"The Wandering Mentor", a Higher Ed blogger, would like a wordpress design

I would like a wordpress design for blogs written by "The Wandering Mentor." that can be easily expanded by me once the initial design is complete.

Here is context which I would like included on the Home/Welcome page: "I started The Wandering Mentor in 2021 to write about the practice of academic advising through the lens of horsemanship. After one year of developing skills as a brand new equestrian, I couldn’t help but notice the similarities between my vocation as an academic advisor and my avocation as a budding equestrian. I hope my musings about my journey in two very different fields will cultivate curiosity, widen your aperture and ignite academic advisors to take their practice to the next level. "

The wordpress will primarily have blogs by myself or guest bloggers writing about academic advising for advisors, but I may widen my audience to include students and families. I'd like to have readers submit questions that I can answer. Depending on interest, I may want to have a section on Horsemanship but that is not truly the focus of this site.

I'd like the feel of the site to be positive, fresh, modern (but not too wild), with the emphasis on Higher Ed/Academic Advising as opposed to equestrian pursuits. I don't want it to feel clunky and blocky like some sites that have to do with education. I'm hoping that readers will have some "aha" moments after reading some of the posts.

I have included my logo files

```html
<!DOCTYPE html>
<html lang="en">
<head>
<meta charset="utf-8">
<title>The Wandering Mentor</title>
<link href="https://fonts.googleapis.com/css2?family=Mulish:wght@400;600;700&family=Oswald:wght@400;700&display=swap" rel="stylesheet">
<style>
:root{
  --gold:#c9a063;
  --gold-soft:#d7b27a;
  --black:#000;
  --band:#1c1c1c;
  --band-2:#181818;
  --text:#e9e9e9;
  --muted:#b4b4b4;
  --input:#3a3a3a;
}
*{box-sizing:border-box;margin:0;padding:0}
html,body{width:1200px;height:4492px;overflow:hidden}
body{position:relative;background:var(--black);color:var(--text);font-family:"Mulish",sans-serif}
.abs{position:absolute}
.ph{position:absolute}
/* nav */
.nav{left:162px;top:14px;display:flex;gap:30px;font-size:13px;color:var(--gold)}
.nav a:first-child{color:#fff}
.nav a{text-decoration:none;color:inherit}
.social{right:162px;top:10px;display:flex;gap:8px}
.social span{width:26px;height:26px;border:1.5px solid var(--gold);border-radius:50%;display:block}
/* hero */
.hero{left:0;top:0;width:1200px;height:600px;background:linear-gradient(180deg,#3b3d2e 0%,#2f3328 45%,#4a4536 100%)}
.hero-logo{left:0;width:1200px;top:230px;text-align:center;font-size:34px;font-weight:700;color:var(--gold);letter-spacing:2px}
.hero-title{left:0;width:1200px;top:392px;text-align:center;font-family:"Oswald",sans-serif;font-size:40px;line-height:50px;color:#fff;font-weight:400}
/* subscribe */
.subscribe{left:0;width:1200px;background:var(--band)}
.envelope{position:absolute}
.sub-title{position:absolute;font-size:30px;color:var(--text)}
.sub-text{position:absolute;font-size:15px;color:var(--text)}
.sub-form{position:absolute;display:flex;height:35px;font-size:12px}
.sub-form .field{width:248px;background:var(--input);color:#ccc;padding:9px 12px}
.sub-form .btn{width:92px;background:var(--gold);color:#111;text-align:center;padding-top:9px;font-weight:600}
/* posts */
.date{font-size:12px;color:var(--gold);font-weight:600}
.post-title{font-size:24px;line-height:29px;color:var(--text)}
.post-title.sm{font-size:17px;line-height:21px}
.excerpt{font-size:12.5px;line-height:21.5px;color:var(--muted)}
.more{display:inline-block;border:1px solid var(--gold);color:var(--gold-soft);font-size:13px;font-weight:600;padding:9px 17px}
.overlay-card .tag{position:absolute;right:0;top:0;background:var(--gold-soft);color:#111;font-size:12px;font-weight:700;padding:8px 14px}
.overlay-card .cap{position:absolute;left:0;width:100%;bottom:20px;text-align:center;font-size:19px;line-height:23px;color:#eee}
/* ad */
.ad{left:208px;top:2429px;width:783px;height:109px;background:#8a8a8a;padding:6px}
.ad-inner{width:100%;height:100%;background:linear-gradient(90deg,#2b2b2b,#404040);position:relative}
.ad-cover{left:24px;top:14px;width:56px;height:70px;background:linear-gradient(135deg,#d8cfbf,#a2907a)}
.ad-head{left:112px;top:32px;font-family:"Oswald",sans-serif;font-weight:700;font-size:25px;color:#fff}
.ad-brand{left:660px;top:12px;font-size:22px;font-weight:700;color:#fff}
.ad-cta{left:612px;top:60px;width:150px;height:24px;background:#f0a33b;color:#fff;font-size:11px;font-weight:700;text-align:center;padding-top:5px}
.load{left:546px;top:3057px;width:106px;height:35px;background:var(--gold-soft);color:#111;font-size:13px;font-weight:700;text-align:center;padding-top:9px}
/* about */
.about-title{left:0;width:1200px;top:3538px;text-align:center;font-size:25px;color:var(--text)}
.about-mark{left:583px;top:3480px;width:34px;height:34px;border:2px solid var(--gold);border-radius:50%}
.about-name{left:628px;top:3640px;font-size:27px;color:var(--gold)}
.about-name small{font-size:19px}
.about-lead{left:630px;top:3688px;width:400px;font-size:16.5px;line-height:23px;color:var(--text)}
.about-body{left:628px;top:3780px;width:410px;font-size:12.5px;line-height:21.5px;color:var(--muted)}
/* footer */
.footer{left:0;top:4081px;width:1200px;height:411px;background:var(--band)}
.foot-links{left:164px;top:4194px;list-style:none;font-size:13px;line-height:30.5px;color:var(--gold)}
.foot-links li:first-child{color:#fff}
.foot-links li:last-child{margin-top:6px}
.foot-logo{left:400px;top:4252px;width:300px;text-align:center;font-size:26px;font-weight:700;color:var(--gold)}
.contact-item{left:826px;display:flex;align-items:center;gap:16px}
.contact-item .ring{width:48px;height:48px;border:1.5px solid var(--gold);border-radius:50%;display:flex;align-items:center;justify-content:center}
.contact-item .lbl{font-size:13px;color:#fff;line-height:22px}
.copy{left:0;width:1200px;top:4438px;text-align:center;font-size:13px;color:#fff}
</style>
</head>
<body>

<!-- Hero -->
<div class="ph hero" role="img" aria-label="Rider leading a horse along a countryside path at dusk"></div>
<nav class="abs nav"><a>Home</a><a>Academic Topics</a><a>Coaching</a><a>About</a><a>Horsemanship</a></nav>
<div class="abs social"><span></span><span></span><span></span><span></span></div>
<div class="abs hero-logo">The Wandering Mentor</div>
<h1 class="abs hero-title">Providing Academic Advising Through The<br>Lens of Horsemanship</h1>

<!-- Subscribe top -->
<section class="abs subscribe" style="top:600px;height:206px">
  <svg class="envelope" style="left:349px;top:47px" width="113" height="110" viewBox="0 0 113 110" fill="none" stroke="#c9a063" stroke-width="3">
    <path d="M4 48 L56 12 L108 48 V106 H4 Z"/><path d="M4 48 L56 82 L108 48"/><path d="M4 106 L44 74 M108 106 L68 74"/>
    <rect x="24" y="4" width="64" height="54" fill="#1c1c1c"/><path d="M36 20 H76 M36 32 H76 M36 44 H66"/>
  </svg>
  <div class="sub-title" style="left:486px;top:40px">Subscribe To Our Blog</div>
  <div class="sub-text" style="left:489px;top:84px">Get the latest tips &amp; updates right to your inbox</div>
  <div class="sub-form" style="left:485px;top:120px"><div class="field">Enter Your email</div><div class="btn">Subscribe</div></div>
</section>

<!-- Featured post 1 -->
<div class="ph" style="left:162px;top:877px;width:440px;height:361px;background:linear-gradient(135deg,#5a3a16,#8a5a24 40%,#2e2416)" role="img" aria-label="White horse with bridle standing among autumn trees"></div>
<div class="abs date" style="left:672px;top:933px">Aug 29, 2021</div>
<h2 class="abs post-title" style="left:631px;top:960px;width:420px">Lorem Ipsum Dolor Sit Amet, Cons Ctetuer Adipiscing Elit</h2>
<p class="abs excerpt" style="left:631px;top:1023px;width:400px">Lorem ipsum dolor sit amet, consectetuer adipiscing elit, sed diam nonummy nibh euismod tincidunt ut laoreet ore magna aliquam erat volutpat. Ut wisi enim ad minim veniam, quis nostrud exerci tation ullamcorper suscipit lobortis nisl ut aliquip ex ea commodo consequat.</p>
<a class="abs more" style="left:631px;top:1142px">Read More</a>

<!-- Two small posts -->
<div class="ph" style="left:162px;top:1280px;width:218px;height:215px;background:linear-gradient(160deg,#5c7a2e,#7a5a30 60%,#4d6a28)" role="img" aria-label="Woman sitting in grass beside a chestnut horse"></div>
<div class="abs date" style="left:427px;top:1285px">Sep 10, 2021</div>
<h3 class="abs post-title sm" style="left:394px;top:1307px;width:200px">Lorem Ipsum Dolor Sit Met, Cons &nbsp;Adipisci.</h3>
<p class="abs excerpt" style="left:394px;top:1355px;width:190px">Lorem ipsum dolor sit amet, ectetuer adipiscing elit, sed diam nonummy nibh euismod tincidunt ut lao.</p>
<a class="abs more" style="left:394px;top:1449px">Read More</a>

<div class="ph" style="left:624px;top:1280px;width:218px;height:215px;background:linear-gradient(160deg,#9aa4b2,#3c4a60 55%,#cfd3d8)" role="img" aria-label="Two colleagues talking in a bright office"></div>
<div class="abs date" style="left:892px;top:1285px">Sep 10, 2021</div>
<h3 class="abs post-title sm" style="left:860px;top:1307px;width:190px">Lorem Ipsum Dolor Sit Met, Cons &nbsp;Adipisci.</h3>
<p class="abs excerpt" style="left:860px;top:1355px;width:185px">Lorem ipsum dolor sit amet, ectetuer adipiscing elit, sed diam nonummy nibh euismod tincidunt ut lao.</p>
<a class="abs more" style="left:860px;top:1449px">Read More</a>

<!-- Overlay cards -->
<div class="abs overlay-card" style="left:162px;top:1540px;width:431px;height:412px">
  <div class="ph" style="inset:0;background:linear-gradient(180deg,#d9dde0,#a88058 55%,#2c2016)" role="img" aria-label="Smiling rider seated on a brown horse"></div>
  <div class="tag">Sep 10, 2021</div>
  <div class="cap">Lorem Ipsum Dolor Sit Amens Ctetuer<br>Adipiscing Elit</div>
</div>
<div class="abs overlay-card" style="left:607px;top:1540px;width:431px;height:412px">
  <div class="ph" style="inset:0;background:linear-gradient(180deg,#e6e6e4,#7d8a9c 55%,#2c3444)" role="img" aria-label="Advisor and student reviewing work on a laptop"></div>
  <div class="tag">Sep 10, 2021</div>
  <div class="cap" style="bottom:30px">Lorem Ipsum Dolor Sit Amens Ctetuer<br>Adipiscing Elit</div>
</div>

<!-- Featured post 2 -->
<div class="abs date" style="left:208px;top:2073px">Sep 11, 2021</div>
<h2 class="abs post-title" style="left:163px;top:2095px;width:400px">Lorem Ipsum Dolor Sit Amet, Cons Ctetuer Adipiscing Elit</h2>
<p class="abs excerpt" style="left:163px;top:2160px;width:400px">Lorem ipsum dolor sit amet, consectetuer adipiscing elit, sed diam nonummy nibh euismod tincidunt ut laoreet ore magna aliquam erat volutpat. Ut wisi enim ad minim veniam, quis nostrud exerci tation ullamcorper suscipit lobortis nisl ut aliquip ex ea commodo consequat.</p>
<a class="abs more" style="left:163px;top:2279px">Read More</a>
<div class="ph" style="left:598px;top:2013px;width:440px;height:362px;background:linear-gradient(180deg,#7a4a32,#5f6a3e 40%,#c8ab82 70%,#b89670)" role="img" aria-label="Rider cantering a chestnut horse in a sand arena before a brick wall"></div>

<!-- Ad -->
<div class="abs ad"><div class="ad-inner">
  <div class="ph ad-cover" role="img" aria-label="Audiobook cover"></div>
  <div class="abs ad-head">ENJOY BOOKS IN A WHOLE NEW WAY</div>
  <div class="abs ad-brand">Listenwell</div>
  <div class="abs ad-cta">2 FREE AUDIOBOOKS</div>
</div></div>

<!-- Three cards -->
<div class="ph" style="left:160px;top:2602px;width:269px;height:194px;background:linear-gradient(180deg,#6f9ad0,#8c8c8c 55%,#b8a486)" role="img" aria-label="Show jumper clearing a fence outdoors"></div>
<div class="ph" style="left:464px;top:2602px;width:269px;height:194px;background:linear-gradient(180deg,#e8eae6,#b89e86 55%,#e2e2e0)" role="img" aria-label="Students working together at a table"></div>
<div class="ph" style="left:767px;top:2602px;width:271px;height:194px;background:linear-gradient(180deg,#4f6b38,#8a5a34 55%,#9b8a70)" role="img" aria-label="Rider on a bay horse at a paddock fence"></div>

<div class="abs date" style="left:163px;top:2818px">January 29, 2021</div>
<h3 class="abs post-title sm" style="left:163px;top:2844px;width:250px">Lorem Ipsum Dolor Sit Met, Cons Ctetuer Adipisci.</h3>
<p class="abs excerpt" style="left:163px;top:2893px;width:250px">Lorem ipsum dolor sit amet, ectetuer adipiscing elit, sed diam nonummy nibh euismod tincidunt ut lao.</p>
<a class="abs more" style="left:163px;top:2970px">Read More</a>

<div class="abs date" style="left:464px;top:2818px">January 29, 2021</div>
<h3 class="abs post-title sm" style="left:464px;top:2844px;width:250px">Lorem Ipsum Dolor Sit Met, Cons Ctetuer Adipisci.</h3>
<p class="abs excerpt" style="left:464px;top:2893px;width:250px">Lorem ipsum dolor sit amet, ectetuer adipiscing elit, sed diam nonummy nibh euismod tincidunt ut lao.</p>
<a class="abs more" style="left:464px;top:2970px">Read More</a>

<div class="abs date" style="left:768px;top:2818px">January 29, 2021</div>
<h3 class="abs post-title sm" style="left:768px;top:2844px;width:250px">Lorem Ipsum Dolor Sit Met, Cons Ctetuer Adipisci.</h3>
<p class="abs excerpt" style="left:768px;top:2893px;width:250px">Lorem ipsum dolor sit amet, ectetuer adipiscing elit, sed diam nonummy nibh euismod tincidunt ut lao.</p>
<a class="abs more" style="left:768px;top:2970px">Read More</a>

<div class="abs load">Load More</div>

<!-- Subscribe bottom -->
<section class="abs subscribe" style="top:3174px;height:227px;background:var(--band-2)">
  <svg class="envelope" style="left:347px;top:58px" width="113" height="110" viewBox="0 0 113 110" fill="none" stroke="#c9a063" stroke-width="3">
    <path d="M4 48 L56 12 L108 48 V106 H4 Z"/><path d="M4 48 L56 82 L108 48"/><path d="M4 106 L44 74 M108 106 L68 74"/>
    <rect x="24" y="4" width="64" height="54" fill="#181818"/><path d="M36 20 H76 M36 32 H76 M36 44 H66"/>
  </svg>
  <div class="sub-title" style="left:489px;top:64px">Subscribe To Our Blog</div>
  <div class="sub-text" style="left:490px;top:116px">Get the latest tips &amp; updates right to your inbox</div>
  <div class="sub-form" style="left:491px;top:156px"><div class="field">Enter Your email</div><div class="btn">Subscribe</div></div>
</section>

<!-- About -->
<div class="abs about-mark"></div>
<h2 class="abs about-title" style="font-weight:400">About The Wandering Mentor</h2>
<div class="ph" style="left:160px;top:3622px;width:440px;height:361px;background:linear-gradient(135deg,#6f5a3e,#c9b39a 45%,#3a2e24)" role="img" aria-label="Author embracing a paint horse outdoors"></div>
<div class="abs about-name">Lena Hartley, <small>Wandering Mentor</small></div>
<p class="abs about-lead">I started The Wandering Mentor in 2021 to write about the practice of academic advising through the lens of horsemanship</p>
<p class="abs about-body">After one year of developing skills as a brand new equestrian, I couldn’t help but notice the similarities between my vocation as an academic advisor and my avocation as a budding equestrian. I hope my musings about my journey in two very different fields will cultivate curiosity, widen your aperture and ignite academic advisors to take their practice to the next level.</p>
<a class="abs more" style="left:626px;top:3920px">Contact Me Today</a>

<!-- Footer -->
<footer class="abs footer"></footer>
<ul class="abs foot-links"><li>Home</li><li>Academic Topics</li><li>Coaching</li><li>About</li><li>Horsemanship</li><li>Contact</li></ul>
<div class="abs foot-logo">The Wandering Mentor</div>
<div class="abs contact-item" style="top:4208px">
  <div class="ring"><svg width="22" height="22" viewBox="0 0 24 24" fill="none" stroke="#c9a063" stroke-width="1.8"><path d="M5 3h4l2 5-3 2a12 12 0 0 0 6 6l2-3 5 2v4a2 2 0 0 1-2 2A17 17 0 0 1 3 5a2 2 0 0 1 2-2z"/></svg></div>
  <div class="lbl">PHONE<br>&nbsp;&nbsp;555-013-2048</div>
</div>
<div class="abs contact-item" style="top:4294px">
  <div class="ring"><svg width="22" height="22" viewBox="0 0 24 24" fill="none" stroke="#c9a063" stroke-width="1.8"><path d="M3 10l9-6 9 6v10H3z"/><path d="M3 10l9 6 9-6"/></svg></div>
  <div class="lbl">EMAIL<br>info@wanderingmentor.com</div>
</div>
<div class="abs copy">Copyright © 2021 The Wandering Mentor. All Rights Reserved.</div>

</body>
</html>
```